Anesthesia Medical Practice Business Card

We need a business card to hand out to surgeons with my basic information. Something that stands out but is not over the top. The medical community is rather conservative. I'd like them to call me first when flipping through their rolodex of anesthesiologists. I'd like the card to communicate confidence, control, professionalism yet serenity. I don't want the card to be pricey to print.

he logo will be provided as a vector graphic in addition to a complete business card design including the logo

Rex Alba Tovell, M.D.
Board Certified Anesthesiologist

(555) 638-2175

rtovell@quillnet.example

Mailing Address:
48317 Pemberly Ave.
Suite 274-6583
Los Angeles, CA 90871

A logo that inegrates my initials perhaps
RT MD
My initials are RT and MD as in Medical Doctor

or
perhaps a physician in surgical mask and cap caring for a patient

Surgeons who need anesthesia services

Medical

• the logo will be provided as a vector graphic in addition to a complete business card design including the logo

Rex Alba Tovell, M.D.

(555) 638-2175

rtovell@quillnet.example

Mailing Address:
48317 Pemberly Ave.
Suite 274-6583
Los Angeles, CA 90871

• A logo that inegrates my initials perhaps
RT MD

or

```html
<!DOCTYPE html>
<html lang="en">
<head>
<meta charset="utf-8">
<title>Rex Alba Tovell, M.D. — Business Card</title>
<link rel="stylesheet" href="https://fonts.googleapis.com/css2?family=Josefin+Sans:wght@300;400&display=swap">
<style>
  :root {
    --backdrop: #3a302b;
    --card: #121212;
    --card-sheen: #262626;
    --ink: #f4f4f2;
    --ink-soft: #b9b9b6;
    --logo-fill: #e9e9e6;
  }
  * { box-sizing: border-box; margin: 0; padding: 0; }
  html, body {
    width: 1200px;
    height: 1000px;
    overflow: hidden;
    background: var(--backdrop);
  }
  .stage {
    width: 1200px;
    height: 1000px;
    display: flex;
    align-items: center;
    justify-content: center;
  }
  .business-card {
    width: 470px;
    height: 800px;
    background: linear-gradient(155deg, var(--card) 0%, var(--card-sheen) 45%, var(--card) 70%);
    color: var(--ink);
    font-family: "Josefin Sans", sans-serif;
    font-weight: 300;
    position: relative;
    padding: 290px 0 0 150px;
  }
  .logo-placeholder {
    display: block;
    width: 110px;
    height: 110px;
    background: var(--logo-fill);
    margin-bottom: 36px;
  }
  .identity { margin-bottom: 26px; }
  .name {
    font-size: 22px;
    font-weight: 400;
    letter-spacing: 0.5px;
  }
  .title {
    font-size: 13px;
    color: var(--ink-soft);
    margin-top: 4px;
    letter-spacing: 0.3px;
  }
  .contact, .address {
    font-size: 13px;
    line-height: 1.7;
    color: var(--ink-soft);
    padding-left: 40px;
  }
  .contact { margin-bottom: 18px; }
</style>
</head>
<body>
  <main class="stage">
    <section class="business-card">
      <div class="logo-placeholder" role="img" aria-label="Practice logo: client's initials monogram"></div>
      <div class="identity">
        <p class="name">Rex Alba Tovell, M.D.</p>
        <p class="title">Board Certified Anesthesiologist</p>
      </div>
      <div class="contact">
        <p class="phone">(555) 638-2175</p>
        <p class="email">rtovell@quillnet.example</p>
      </div>
      <div class="address">
        <p>Mailing Address:</p>
        <p>48317 Pemberly Ave.</p>
        <p>Suite 274-6583</p>
        <p>Los Angeles, CA 90871</p>
      </div>
    </section>
  </main>
</body>
</html>
```